Stationery Design Project

I am looking for stationary design for an automotive collision repair company. This needs to work with my business cards just designed here. I've attached. I need 8.5 x 11 stationary and corissponding envelopes. a jot tab note pad also. Our companies focus is very high end customer service driven . Our customer base is 35-65 middle to high income. Please include company name, logo, address, phone number, web address. The business card is two greys with green and white writing. I invision a light grey background with a darker grey band on it that contains the logo.
Updates

I justĀ 

Why is no one touching this project

Target Market(s)

60%. Women 40% men. Age 35-60

Industry/Entity Type

Automotive

Requirements
Must have
• Tie in with business cards. So it needs grey tones with green and white logo. Name, address, phone and web address. Must have 8.5 x 11 paper and envelopes.
Nice to have
• Jot tab notes

```html
<!DOCTYPE html>
<html lang="en">
<head>
<meta charset="utf-8">
<title>Keelwright Auto — Stationery Set</title>
<link rel="stylesheet" href="https://fonts.googleapis.com/css2?family=Arimo:wght@400;700&display=swap">
<style>
  :root{
    --page:#f3f3f3;
    --grey:#858585;
    --green:#7ab230;
    --green-dark:#6a9c28;
    --white:#ffffff;
    --rule:#9cc45c;
    --shadow:0 6px 14px rgba(0,0,0,.18);
  }
  *{box-sizing:border-box;margin:0;padding:0}
  html,body{width:1154px;height:1200px;overflow:hidden}
  body{background:var(--page);font-family:"Arimo",Arial,sans-serif;position:relative}

  .sheet{position:absolute;overflow:hidden;box-shadow:var(--shadow);background:var(--green)}
  .sheet svg.wave{position:absolute;inset:0;width:100%;height:100%}

  .brand{position:absolute;color:var(--white);font-weight:700;white-space:nowrap;line-height:1}
  .brand-tagline{display:block;font-weight:400;font-size:7px;letter-spacing:1.6px;margin-top:4px;text-transform:uppercase}

  /* Letterhead */
  .letterhead{left:109px;top:79px;width:455px;height:576px}
  .letterhead .brand{left:30px;top:52px;font-size:24px}
  .letterhead .rule{position:absolute;left:0;top:208px;width:196px;height:1px;background:var(--rule)}
  .letterhead .contact{position:absolute;left:305px;top:505px;color:var(--white);font-size:7.5px;line-height:10px}
  .contact-name{font-size:17px;letter-spacing:.6px;line-height:1;margin-bottom:6px}

  /* Folder */
  .folder{left:603px;top:79px;width:453px;height:576px;background:var(--grey)}
  .folder .brand{right:30px;top:275px;font-size:12px}

  /* Envelopes */
  .envelope-wave{left:107px;top:738px;width:459px;height:193px}
  .envelope-wave .brand{left:18px;top:127px;font-size:12px}
  .envelope-band{left:599px;top:738px;width:459px;height:193px}
  .envelope-band .brand{right:18px;top:20px;font-size:12px}
  .envelope-band .rule{position:absolute;right:18px;top:62px;width:110px;height:1px;background:var(--rule)}

  /* Jot tab pads */
  .jot-pad{width:178px;height:176px}
  .jot-pad.loose{left:309px;top:963px}
  .jot-pad.bound{left:668px;top:963px}
  .jot-pad .brand{right:10px;bottom:14px;font-size:9px}
</style>
</head>
<body>

  <section class="sheet letterhead" aria-label="Letterhead">
    <svg class="wave" viewBox="0 0 455 576" preserveAspectRatio="none" aria-hidden="true">
      <path d="M0 0H455V70C380 90 300 150 200 175C120 195 50 195 0 190Z" fill="var(--grey)"/>
    </svg>
    <div class="brand">Keelwright Auto<span class="brand-tagline">Quality repair with care</span></div>
    <div class="rule"></div>
    <address class="contact" style="font-style:normal">
      <div class="contact-name">Keelwright Auto</div>
      7781 Harbour Lane, Leeds<br>
      office: 0113-555-0192<br>
      web: www.keelwrightauto.com<br>
      e-mail: hello@keelwrightauto.com
    </address>
  </section>

  <section class="sheet folder" aria-label="Presentation folder">
    <div class="brand">Keelwright Auto</div>
  </section>

  <section class="sheet envelope-wave" aria-label="Envelope, front">
    <svg class="wave" viewBox="0 0 459 193" preserveAspectRatio="none" aria-hidden="true">
      <path d="M0 0H459V75C380 85 320 95 250 115C170 140 100 160 0 150Z" fill="var(--grey)"/>
    </svg>
    <div class="brand">Keelwright Auto</div>
  </section>

  <section class="sheet envelope-band" aria-label="Envelope, back">
    <svg class="wave" viewBox="0 0 459 193" preserveAspectRatio="none" aria-hidden="true">
      <path d="M0 0H459V48H20Q0 48 0 30Z" fill="var(--grey)"/>
    </svg>
    <div class="brand">Keelwright Auto</div>
    <div class="rule"></div>
  </section>

  <section class="sheet jot-pad loose" aria-label="Jot tab note">
    <svg class="wave" viewBox="0 0 178 176" preserveAspectRatio="none" aria-hidden="true">
      <path d="M0 115C40 100 70 120 110 125C140 128 160 120 178 125V176H0Z" fill="var(--grey)"/>
    </svg>
    <div class="brand">Keelwright Auto</div>
  </section>

  <section class="sheet jot-pad bound" aria-label="Jot tab note pad">
    <svg class="wave" viewBox="0 0 178 176" preserveAspectRatio="none" aria-hidden="true">
      <path d="M0 115C40 100 70 120 110 125C140 128 160 120 178 125V176H0Z" fill="var(--grey)"/>
    </svg>
    <div class="brand">Keelwright Auto</div>
  </section>

</body>
</html>
```